Innovative law firm needs eye catching, professional and fun ad design

Veltramor LLP is an innovative law firm based in Toronto, Canada. We were founded in 2005 and have grown to 30 lawyers. Veltramor offers an alternative to traditional law firms by providing our clients with access to experienced, business-minded lawyers at affordable rates and with flexible working arrangements. We vigilantly maintain a low overhead cost structure and use only lawyers that have built successful careers at some of the most respected Canadian law firms and corporate legal departments. More information is available at www.veltramorllp-example.com.

We require a 4.5" (width) x 7.75" (height) colour advertisement that will be placed in a weekly legal magazine with over 45,000 readers. The ad is intended to attract new job applicants to our growing firm. We want the design to reflect our innovative firm model and revolutionary spirit in order to attract candidates that are the right fit with our culture.

The ad must incorporate the draft text below (to be finalized with the selected designer) as well as our logo and the attached image (which we will purchase and provide to the selected designer).

Draft text:

***
Remember when anything was possible?

Veltramor LLP is leading a revolution in legal services. We are turning the legal profession on its head by having an open dialogue with our clients and focusing on their legal needs – in the way they want. To steer our uprising, we only enlist the very best. In the last year, we received over 300 resumes from daring individuals hoping to join our growing band of renegades. Just 2% of those applicants were welcomed into our family.

Lawyers working with Veltramor share the following traits:
• 10+ years of combined experience in private practice at a large Bay St firm and senior in-house roles,
• a practical approach to solving clients’ legal problems,
• an obsession for providing exceptional value and service to clients, and
• an entrepreneurial and audacious spirit.

We are in need of an IT LAWYER with experience in outsourcing, licensing, digital media and SAAS-based services.

Interested in joining the revolution? Review our Pledge of Ideals at veltramorllp-example.com/charter. This doesn't motivate you into action? Then you are clearly not cut out for our movement. However, if our Charter inspires you to dream big, then please apply through our careers page.

***

Target Market(s)

Lawyers who are fed up with the status quo offered at regular firms

Industry/Entity Type

Law Firm

Requirements
Must have
• Our logo and the attached image (we will purchase the image once we have selected the designer and determined the appropriate size)
Nice to have
• Should also incorporate the Quandel logos

Make the text of the position being advertised stand out (bold, larger size)

```html
<!DOCTYPE html>
<html lang="en">
<head>
<meta charset="utf-8">
<title>Veltramor LLP – IT Lawyer Recruitment Ad</title>
<link href="https://fonts.googleapis.com/css2?family=Oswald:wght@600;700&family=Arimo:ital,wght@0,400;0,700;1,400;1,700&display=swap" rel="stylesheet">
<style>
  :root {
    --navy: #1c2f5a;
    --red: #d0202e;
    --blue: #2b6db3;
    --light-blue: #5fa2d8;
    --ink: #1e1e1e;
    --white: #ffffff;
    --badge: #8a8f96;
  }
  * { box-sizing: border-box; margin: 0; padding: 0; }
  html, body { width: 698px; height: 1200px; overflow: hidden; background: var(--white); }
  body { font-family: "Arimo", Arial, sans-serif; color: var(--ink); }
  .ad { width: 698px; height: 1200px; display: flex; flex-direction: column; }

  .headline {
    height: 56px; display: flex; align-items: center; justify-content: center;
    font-family: "Oswald", "Arial Narrow", sans-serif; font-weight: 700;
    font-size: 36px; letter-spacing: 0.5px; color: var(--navy); text-transform: uppercase;
  }
  .headline em { color: var(--red); font-style: italic; padding: 0 6px; }

  .hero {
    height: 420px;
    background: linear-gradient(180deg, #9fb6c6 0%, #c3d0d6 45%, #b8b2a4 70%, #7d776d 100%);
  }

  .intro {
    background: var(--blue); color: var(--white);
    padding: 22px 40px; font-size: 17.5px; line-height: 1.42;
  }
  .intro b { font-style: italic; }

  .traits { padding: 20px 40px 18px; font-size: 16.5px; line-height: 1.4; }
  .traits ul { list-style: none; }
  .traits li { padding-left: 16px; text-indent: -16px; }
  .traits li::before { content: "•"; display: inline-block; width: 16px; text-indent: 0; }

  .opening {
    background: var(--light-blue); color: var(--white);
    padding: 16px 40px; font-size: 18px; line-height: 1.35;
  }
  .opening .role {
    font-family: "Oswald", "Arial Narrow", sans-serif; font-weight: 700;
    font-size: 34px; color: var(--navy); letter-spacing: 0.5px; vertical-align: -3px;
  }

  .closing { position: relative; flex: 1; padding: 18px 40px 0; text-align: center; font-size: 16px; line-height: 1.4; }
  .closing .link { color: var(--red); font-weight: 700; font-size: 17px; }
  .closing .lead { font-weight: 700; }

  .footer { position: absolute; left: 0; right: 0; bottom: 16px; height: 100px; }
  .badge { position: absolute; bottom: 0; width: 92px; height: 92px; }
  .badge.left { left: 30px; }
  .badge.right { right: 30px; }
  .wordmark {
    position: absolute; left: 50%; bottom: 30px; transform: translateX(-50%);
    display: flex; align-items: center; gap: 10px;
    font-family: "Arimo", Arial, sans-serif; font-weight: 700; font-size: 30px;
    color: var(--navy); letter-spacing: 2px; text-transform: uppercase;
  }
  .wordmark .dot { width: 16px; height: 16px; border-radius: 50%; background: var(--red); }
</style>
</head>
<body>
<main class="ad">
  <h1 class="headline">Remember when <em>anything</em> was possible?</h1>

  <div class="hero" role="img" aria-label="Photograph of a child in a flight helmet and goggles wearing cardboard wings on an open road, with another child in the distance"></div>

  <section class="intro">
    <p>Veltramor LLP is leading a <b>revolution</b> in legal services. We are turning the legal profession on its head by having an open dialogue with our clients and focusing on their legal needs – in the way <b>they</b> want. To steer our uprising, we only enlist the very best. In the last year, we received over 300 resumes from daring individuals hoping to join our growing band of renegades. Just <b>2%</b> of those applicants were welcomed into our family.</p>
  </section>

  <section class="traits">
    <p>Lawyers working with Veltramor share the following traits:</p>
    <ul>
      <li>10+ years of combined experience in private practice at a large Bay St firm and senior in-house roles,</li>
      <li>a practical approach to solving clients’ legal problems,</li>
      <li>an obsession for providing exceptional value and service to clients, and</li>
      <li>an entrepreneurial and audacious spirit.</li>
    </ul>
  </section>

  <section class="opening">
    <p>We are in need of an <span class="role">IT LAWYER</span> with experience in outsourcing, licensing, digital media and SAAS-based services.</p>
  </section>

  <section class="closing">
    <p>Interested in joining the revolution? Review our Pledge of Ideals at</p>
    <p class="link">veltramorllp-example.com/charter</p>
    <p class="lead">This doesn’t motivate you into action? Then you are clearly not cut out for our movement.</p>
    <p>However, if our Pledge inspires you to dream big,<br>then please apply through our careers page.</p>

    <div class="footer">
      <svg class="badge left" viewBox="0 0 92 92" aria-label="Quandel 200 award badge, 2012" role="img">
        <rect x="0" y="0" width="92" height="92" fill="var(--badge)"/>
        <rect x="0" y="0" width="92" height="20" fill="var(--navy)"/>
      </svg>
      <div class="wordmark"><span class="dot"></span>Veltramor</div>
      <svg class="badge right" viewBox="0 0 92 92" aria-label="Quandel 500 award badge, 2013" role="img">
        <rect x="0" y="0" width="92" height="92" fill="var(--badge)"/>
        <rect x="0" y="0" width="92" height="20" fill="var(--navy)"/>
      </svg>
    </div>
  </section>
</main>
</body>
</html>
```